Cedar Lantern Letterhead

I just need letterhead for my integrative psychiatry business. I'm going to use this to do mailings to other doctors, as well as send letters to patients. Thank you

Business

```html
<!DOCTYPE html>
<html lang="en">
<head>
<meta charset="utf-8">
<title>Cedar Lantern Letterhead</title>
<link rel="stylesheet" href="https://fonts.googleapis.com/css2?family=Open+Sans:wght@400;600;700&family=Pinyon+Script&display=swap">
<style>
  :root {
    --paper: #ffffff;
    --ink: #2b2b2b;
    --name-ink: #3a3a3a;
    --leaf-green: #5e8f2c;
    --bark-brown: #7a5230;
    --rule: #c9c2b4;
    --watermark: #efeae1;
    --watermark-soft: rgba(239, 234, 225, 0);
  }
  * { box-sizing: border-box; margin: 0; padding: 0; }
  html, body {
    width: 872px;
    height: 1200px;
    overflow: hidden;
    background: var(--paper);
  }
  .letterhead {
    position: relative;
    width: 872px;
    height: 1200px;
    background: var(--paper);
    font-family: "Open Sans", Arial, sans-serif;
    color: var(--ink);
  }
  .brand {
    position: absolute;
    left: 48px;
    top: 58px;
    display: flex;
    align-items: center;
    gap: 14px;
  }
  .brand-dot {
    width: 58px;
    height: 58px;
    border-radius: 50%;
    background: var(--leaf-green);
  }
  .brand-name {
    font-size: 26px;
    font-weight: 600;
    color: var(--bark-brown);
    letter-spacing: 0.3px;
  }
  .practitioner {
    position: absolute;
    right: 46px;
    top: 50px;
    text-align: right;
  }
  .practitioner-name {
    font-family: "Pinyon Script", cursive;
    font-size: 36px;
    line-height: 1.1;
    color: var(--name-ink);
  }
  .credentials {
    margin-top: 6px;
    font-size: 13px;
    font-weight: 600;
    line-height: 1.5;
    color: var(--ink);
  }
  .website {
    margin-top: 14px;
    font-size: 14.5px;
    font-weight: 600;
    color: var(--leaf-green);
  }
  .header-rule {
    position: absolute;
    left: 40px;
    right: 40px;
    top: 196px;
    height: 2px;
    background: var(--rule);
  }
  .watermark {
    position: absolute;
    left: 0;
    bottom: 0;
    width: 500px;
    height: 650px;
    background: radial-gradient(ellipse 62% 58% at 32% 48%, var(--watermark) 0%, var(--watermark) 50%, var(--watermark-soft) 100%);
  }
  .footer-contact {
    position: absolute;
    left: 0;
    right: 0;
    bottom: 44px;
    text-align: center;
    font-size: 14.5px;
    font-weight: 600;
    line-height: 1.55;
    color: var(--ink);
  }
</style>
</head>
<body>
  <main class="letterhead">
    <div class="watermark" role="img" aria-label="Faint decorative tree motif in warm beige"></div>

    <header>
      <div class="brand">
        <span class="brand-dot"></span>
        <span class="brand-name">Cedar Lantern</span>
      </div>
      <div class="practitioner">
        <p class="practitioner-name">Marisol Theveney, MD</p>
        <p class="credentials">
          Diplomat, Northfield Council of Mind Medicine and<br>
          Diplomat, Pacific Guild of Integrative and Whole-Person Care
        </p>
        <p class="website">www.cedarlanternwellness.com</p>
      </div>
      <div class="header-rule"></div>
    </header>

    <footer class="footer-contact">
      <p>2870 Alder Crest Drive, Suite 210, Fair Oaks, CA 95628</p>
      <p>Tel: 916-555-0142, 916-555-0187</p>
    </footer>
  </main>
</body>
</html>
```